Business Card for Corinne Waldo

Name: Corinne Waldo
Title: Realtor
Email: Corinne@CorinneWaldoRE.example
Phone: 555-318-7492

On the front of the business card, I would like the photo, the contact information and the Corinne Waldo Logo. The backside is required to have the Broker logo and the required logos. Please use the colors from the logo design. Our company has a classy, professional look.

```html
<!DOCTYPE html>
<html lang="en">
<head>
<meta charset="utf-8">
<title>Corinne Waldo – Business Card</title>
<link href="https://fonts.googleapis.com/css2?family=Cinzel:wght@400;500&family=Montserrat:wght@400;500&display=swap" rel="stylesheet">
<style>
  :root {
    --backdrop: #3b3b3b;
    --card: #161616;
    --card-deep: #0f0f0f;
    --crimson: #c8102e;
    --ink-light: #f2f2f2;
    --ink-soft: #d9d9d9;
    --photo-light: #9a9a9a;
    --photo-dark: #2a2a2a;
  }
  * { box-sizing: border-box; margin: 0; padding: 0; }
  html, body { width: 1200px; height: 801px; overflow: hidden; }
  body {
    background: var(--backdrop);
    position: relative;
    font-family: "Montserrat", sans-serif;
  }
  .card {
    position: absolute;
    top: 246px;
    width: 540px;
    height: 309px;
    background: var(--card);
    border: 2px solid var(--crimson);
    overflow: hidden;
  }
  .card-front { left: 40px; }
  .card-back { left: 620px; background: var(--card-deep); }

  /* Front */
  .agent-photo {
    position: absolute;
    right: 0; top: 0;
    width: 290px; height: 230px;
    background: radial-gradient(ellipse at 45% 35%, var(--photo-light) 0%, #5e5e5e 40%, var(--photo-dark) 80%, transparent 100%);
    -webkit-mask-image: linear-gradient(to bottom, #000 60%, transparent 100%);
    mask-image: linear-gradient(to bottom, #000 60%, transparent 100%);
  }
  .brand-lockup {
    position: absolute;
    left: 34px; top: 118px;
    display: flex; align-items: center; gap: 12px;
  }
  .brand-dot {
    width: 34px; height: 34px;
    border: 2px solid var(--crimson);
    border-radius: 50%;
  }
  .brand-name {
    font-family: "Cinzel", serif;
    font-size: 24px;
    color: var(--crimson);
    letter-spacing: 1px;
    line-height: 1;
  }
  .brand-rule {
    display: flex; align-items: center; gap: 6px;
    margin-top: 4px;
  }
  .brand-rule span.line { height: 1px; width: 150px; background: var(--ink-soft); }
  .brand-rule span.tag {
    font-family: "Cinzel", serif;
    font-size: 9px; color: var(--ink-light); letter-spacing: 1px;
  }
  .agent-block { position: absolute; left: 46px; top: 186px; }
  .agent-name {
    font-family: "Cinzel", serif;
    font-size: 17px; color: var(--crimson); letter-spacing: 1px;
  }
  .agent-title { font-size: 11px; color: var(--ink-light); margin-top: 2px; }
  .contact-list { list-style: none; position: absolute; left: 46px; top: 236px; }
  .contact-list li {
    display: flex; align-items: center; gap: 7px;
    font-size: 11px; color: var(--ink-light); line-height: 19px;
  }
  .contact-list svg { width: 10px; height: 10px; fill: var(--crimson); }

  /* Back */
  .broker-lockup {
    position: absolute;
    left: 0; right: 0; top: 70px;
    text-align: center;
  }
  .broker-dot {
    width: 92px; height: 92px;
    border: 3px solid var(--ink-light);
    border-radius: 50%;
    margin: 0 auto 18px;
  }
  .broker-name {
    font-family: "Cinzel", serif;
    font-size: 26px; color: var(--ink-light); letter-spacing: 3px;
  }
  .broker-tag {
    font-family: "Cinzel", serif;
    font-size: 11px; color: var(--ink-light); letter-spacing: 2px; margin-top: 2px;
  }
  .badge-row {
    position: absolute; right: 16px; bottom: 62px;
    display: flex; gap: 6px; align-items: center;
  }
  .badge { background: var(--ink-light); height: 20px; }
  .badge-a { width: 22px; }
  .badge-b { width: 20px; }
  .badge-c { width: 40px; }
</style>
</head>
<body>
  <section class="card card-front">
    <div class="agent-photo" role="img" aria-label="Black and white portrait photograph of the realtor"></div>

    <div class="brand-lockup">
      <div class="brand-dot"></div>
      <div>
        <div class="brand-name">CORINNE WALDO</div>
        <div class="brand-rule"><span class="line"></span><span class="tag">REAL ESTATE</span></div>
      </div>
    </div>

    <div class="agent-block">
      <div class="agent-name">CORINNE WALDO</div>
      <div class="agent-title">Realtor</div>
    </div>

    <ul class="contact-list">
      <li>
        <svg viewBox="0 0 24 24"><path d="M6.6 10.8a15 15 0 0 0 6.6 6.6l2.2-2.2a1 1 0 0 1 1-.25 11.4 11.4 0 0 0 3.6.57 1 1 0 0 1 1 1V20a1 1 0 0 1-1 1A17 17 0 0 1 3 4a1 1 0 0 1 1-1h3.5a1 1 0 0 1 1 1c0 1.25.2 2.45.57 3.57a1 1 0 0 1-.25 1z"/></svg>
        555-318-7492
      </li>
      <li>
        <svg viewBox="0 0 24 24"><path d="M2 5h20v14H2z M2 5l10 8 10-8" /></svg>
        Corinne@CorinneWaldoRE.example
      </li>
      <li>
        <svg viewBox="0 0 24 24"><circle cx="12" cy="12" r="10"/></svg>
        www.CorinneWaldoRE.example
      </li>
    </ul>
  </section>

  <section class="card card-back">
    <div class="broker-lockup">
      <div class="broker-dot"></div>
      <div class="broker-name">HOLLIS MARLOWE</div>
      <div class="broker-tag">REAL ESTATE</div>
    </div>
    <div class="badge-row">
      <div class="badge badge-a"></div>
      <div class="badge badge-b"></div>
      <div class="badge badge-c"></div>
    </div>
  </section>
</body>
</html>
```